New business card for civil engineering company - "Keystone Audit"

We need a business card designed for our new structural engineering company.

The company name is "Keystone Audit" logo files attached.

We would like the following:
* Two-sided card
* Simple design

Information to be placed on the card:
Name - Marcus Dellow
Job Title - Director / Structural Engineer
Credentials - BEng(Hons), CPEng, CMengNZ, IntPE(NZ)
Email - marcus.dellow@keystoneaudit.co.nz
mobile - 0219364058
website - www.keystoneaudit.co.nz

```html
<!DOCTYPE html>
<html lang="en">
<head>
<meta charset="utf-8">
<title>Keystone Audit — Business Card</title>
<link href="https://fonts.googleapis.com/css2?family=Exo+2:wght@700&family=Open+Sans:wght@400;600&display=swap" rel="stylesheet">
<style>
  :root {
    --stage: #e4e5e7;
    --card: #2b4c77;
    --ink: #ffffff;
    --ink-soft: #d6e1ef;
    --accent: #3d8fd6;
    --shadow: rgba(0, 0, 0, 0.28);
  }
  * { box-sizing: border-box; margin: 0; padding: 0; }
  html, body {
    width: 1200px; height: 800px; overflow: hidden;
    background: var(--stage);
  }
  .canvas {
    position: relative; width: 1200px; height: 800px;
    background: radial-gradient(ellipse at 50% 40%, #f6f6f7 0%, var(--stage) 60%, #c9cacc 100%);
  }
  .card {
    position: absolute; width: 400px; height: 228px;
    background: var(--card);
    box-shadow: 0 6px 14px var(--shadow);
    color: var(--ink);
    font-family: "Open Sans", sans-serif;
  }
  .card--front { left: 170px; top: 286px; }
  .card--back { left: 630px; top: 286px; }

  .brand { position: absolute; }
  .brand__name {
    display: flex; align-items: center; gap: 7px;
    font-family: "Exo 2", sans-serif; font-weight: 700;
    font-size: 20px; letter-spacing: 0.5px; color: var(--ink);
    text-transform: uppercase;
  }
  .brand__mark { width: 10px; height: 10px; background: var(--accent); }
  .brand__tagline {
    margin-top: 3px; font-size: 7px; letter-spacing: 2px;
    color: var(--ink-soft); text-transform: uppercase; font-weight: 600;
  }
  .card--front .brand { left: 100px; top: 150px; }
  .card--back .brand { left: 28px; top: 156px; }
  .card--back .brand__name { font-size: 16px; }

  .person { position: absolute; right: 28px; top: 24px; text-align: right; }
  .person__name {
    font-family: "Exo 2", sans-serif; font-weight: 700;
    font-size: 21px; letter-spacing: 0.5px; text-transform: uppercase;
  }
  .person__role { font-size: 10px; color: var(--ink-soft); margin-top: 4px; }
  .person__credentials { font-size: 7px; color: var(--ink-soft); margin-top: 4px; }

  .contact { position: absolute; left: 188px; top: 152px; list-style: none; }
  .contact__item {
    display: flex; align-items: center; gap: 9px;
    font-size: 10.5px; line-height: 17px; color: var(--ink);
  }
  .contact__icon { width: 9px; height: 9px; flex: none; }
</style>
</head>
<body>
<main class="canvas">
  <section class="card card--front" aria-label="Card front">
    <div class="brand">
      <div class="brand__name"><span class="brand__mark"></span>Keystone Audit</div>
      <div class="brand__tagline">Peer Review Specialists</div>
    </div>
  </section>

  <section class="card card--back" aria-label="Card back">
    <div class="person">
      <h1 class="person__name">Marcus Dellow</h1>
      <p class="person__role">Director / Structural Engineer</p>
      <p class="person__credentials">BEng(Hons), CPEng, CMengNZ, IntPE(NZ)</p>
    </div>

    <div class="brand">
      <div class="brand__name"><span class="brand__mark"></span>Keystone Audit</div>
      <div class="brand__tagline">Peer Review Specialists</div>
    </div>

    <ul class="contact">
      <li class="contact__item">
        <svg class="contact__icon" viewBox="0 0 10 10"><rect x="0.5" y="2" width="9" height="6" fill="var(--accent)"/><path d="M0.5 2 L5 5.5 L9.5 2" fill="none" stroke="var(--card)" stroke-width="0.9"/></svg>
        marcus.dellow@keystoneaudit.co.nz
      </li>
      <li class="contact__item">
        <svg class="contact__icon" viewBox="0 0 10 10"><rect x="2.8" y="0.5" width="4.4" height="9" rx="0.8" fill="none" stroke="var(--accent)" stroke-width="1"/><rect x="4.3" y="7.3" width="1.4" height="1" fill="var(--accent)"/></svg>
        0219364058
      </li>
      <li class="contact__item">
        <svg class="contact__icon" viewBox="0 0 10 10"><circle cx="5" cy="5" r="4.3" fill="none" stroke="var(--accent)" stroke-width="1"/><ellipse cx="5" cy="5" rx="1.8" ry="4.3" fill="none" stroke="var(--accent)" stroke-width="0.8"/><path d="M0.7 5 H9.3" stroke="var(--accent)" stroke-width="0.8"/></svg>
        www.keystoneaudit.co.nz
      </li>
    </ul>
  </section>
</main>
</body>
</html>
```